Website Redesign For Motorbike Rental Company In Thailand

We are a motorbike rental start up in Phuket, Thailand named RIDE ON.

We cater to the tourist and even ex pats that want to rent a motorbike for as short as only 3 days up to 1 year at a time.

We want a website that makes it a very simple ordering process for the customer. Be able to order a motorbike rental without scrolling down...

Simple, attractive design that builds trust and credibility is huge.

Please check this google doc for the CONTENT: https://files.plomvark.example/doc/7KqW3rTzLm92XbVnPc4HsJd8FgYe0aRuNtQiMoEwZ1y/view?mode=share

Target Market(s)

Tourists In Thailand & Expats In Thailand

Industry/Entity Type

motorbike rental, motorcycle rental

Number of Pages Required

1 page

Requirements
Must have
• Must have a thailand phuket theme or feel
Nice to have
• We want a website that makes it a very simple ordering process for the customer. Be able to order a motorbike rental without scrolling down... Simple, attractive design that builds trust and credibility is huge.
Should not have
• na

```html
<!DOCTYPE html>
<html lang="en">
<head>
<meta charset="utf-8">
<title>RIDE ON – Motorbike Rentals in Phuket</title>
<link href="https://fonts.googleapis.com/css2?family=Kumbh+Sans:wght@400;500;600;700&display=swap" rel="stylesheet">
<style>
  :root{
    --orange:#f47216;
    --black:#000;
    --white:#fff;
    --field:#f1f1f1;
    --muted:#6d6d72;
    --ink:#1a1a1a;
    --alt-pay-bg:#e6f4fd;
    --cash:#6dd38a;
  }
  *{box-sizing:border-box;margin:0;padding:0}
  html,body{width:1200px;height:801px;overflow:hidden}
  body{font-family:"Kumbh Sans",sans-serif;background:var(--black);color:var(--white);position:relative}

  .hero-photo{position:absolute;left:0;top:49px;width:1200px;height:691px;
    background:
      radial-gradient(ellipse 260px 320px at 620px 340px, rgba(150,18,24,.75), transparent 70%),
      radial-gradient(ellipse 200px 200px at 1080px 420px, rgba(120,20,26,.55), transparent 70%),
      linear-gradient(110deg,#26282e 0%,#1e2025 40%,#2a2c33 70%,#18191d 100%);}

  .topbar{position:absolute;left:0;top:0;width:1200px;height:49px;background:var(--black)}

  .brand{position:absolute;left:76px;top:52px;display:flex;align-items:center;gap:8px}
  .brand-dot{width:22px;height:22px;border-radius:50%;background:var(--orange)}
  .brand-name{font-size:26px;font-weight:700;color:var(--orange);letter-spacing:.5px;line-height:1}

  .nav{position:absolute;top:57px;left:460px;display:flex}
  .nav a{color:var(--white);text-decoration:none;font-size:15px;font-weight:500;letter-spacing:.2px}
  .nav a+a{margin-left:46px}
  .btn-delivery{position:absolute;left:977px;top:42px;width:144px;height:50px;border-radius:25px;
    background:var(--orange);color:var(--white);font-size:15px;font-weight:600;
    display:flex;align-items:center;justify-content:center;text-decoration:none}

  .headline{position:absolute;left:76px;top:215px;font-size:58px;font-weight:600;line-height:75px;letter-spacing:.3px;white-space:nowrap}

  .features{position:absolute;left:74px;top:386px;list-style:none}
  .features li{display:flex;align-items:center;gap:11px;font-size:21px;height:40px;font-weight:400;white-space:nowrap}
  .features svg{width:19px;height:19px;flex:none}

  .payment{position:absolute;left:773px;top:217px;width:351px;height:434px;background:var(--white);border-radius:8px;color:var(--ink)}
  .payment h2{position:absolute;left:27px;top:22px;font-size:19px;font-weight:600}
  .field{background:var(--field);border-radius:3px;height:40px;display:flex;align-items:center;padding:0 10px;
    font-size:15px;color:var(--muted);position:absolute;left:27px;width:293px}
  .field .mark{position:absolute;right:12px;width:16px;height:16px;border-radius:50%;background:var(--orange)}
  .field-name{top:62px}
  .field-number{top:112px}
  .field-exp{top:162px;width:142px}
  .field-cvc{top:162px;left:178px;width:142px}
  .other{position:absolute;left:27px;top:224px;font-size:14px;font-weight:600}
  .opt{position:absolute;left:27px;width:293px;height:40px;border-radius:3px;display:flex;align-items:center;justify-content:center;font-size:15px;font-weight:600}
  .opt-alt{top:251px;background:var(--alt-pay-bg);color:var(--ink)}
  .opt-cash{top:301px;background:var(--cash);color:var(--white)}
  .btn-checkout{position:absolute;left:82px;top:366px;width:184px;height:40px;border-radius:20px;background:var(--orange);
    color:var(--white);font-size:15px;font-weight:600;display:flex;align-items:center;justify-content:center}

  .areas{position:absolute;left:0;top:740px;width:1200px;height:61px;background:var(--orange);
    display:flex;align-items:center;padding-left:76px;font-size:16.2px;font-weight:500;letter-spacing:.35px;white-space:nowrap}
  .areas strong{font-weight:700;margin-right:5px}
</style>
</head>
<body>
  <div class="hero-photo" role="img" aria-label="Dark moody photo of a red sport motorbike in a garage"></div>
  <div class="topbar"></div>

  <div class="brand"><span class="brand-dot"></span><span class="brand-name">RIDE ON</span></div>

  <nav class="nav">
    <a href="#">MOTORBIKES</a><a href="#">SCOOTERS</a><a href="#">CARS</a><a href="#">FAQ</a><a href="#">ABOUT</a>
  </nav>
  <a class="btn-delivery" href="#">DELIVERY</a>

  <h1 class="headline">Fast Motorbike Rentals<br>In Phuket, Thailand</h1>

  <ul class="features">
    <li><svg viewBox="0 0 20 20"><circle cx="10" cy="10" r="8.5" fill="none" stroke="#f47216" stroke-width="1.6"/><path d="M6 10.2l3 3 6-6.5" fill="none" stroke="#f47216" stroke-width="1.8" stroke-linecap="round" stroke-linejoin="round"/></svg>Free Delivery &amp; Pick Up Anywhere In Phuket</li>
    <li><svg viewBox="0 0 20 20"><circle cx="10" cy="10" r="8.5" fill="none" stroke="#f47216" stroke-width="1.6"/><path d="M6 10.2l3 3 6-6.5" fill="none" stroke="#f47216" stroke-width="1.8" stroke-linecap="round" stroke-linejoin="round"/></svg>Free High Quality Helmet Included</li>
    <li><svg viewBox="0 0 20 20"><circle cx="10" cy="10" r="8.5" fill="none" stroke="#f47216" stroke-width="1.6"/><path d="M6 10.2l3 3 6-6.5" fill="none" stroke="#f47216" stroke-width="1.8" stroke-linecap="round" stroke-linejoin="round"/></svg>Free Unlimited Mileage</li>
    <li><svg viewBox="0 0 20 20"><circle cx="10" cy="10" r="8.5" fill="none" stroke="#f47216" stroke-width="1.6"/><path d="M6 10.2l3 3 6-6.5" fill="none" stroke="#f47216" stroke-width="1.8" stroke-linecap="round" stroke-linejoin="round"/></svg>Easy &amp; Quick Online Booking</li>
    <li><svg viewBox="0 0 20 20"><circle cx="10" cy="10" r="8.5" fill="none" stroke="#f47216" stroke-width="1.6"/><path d="M6 10.2l3 3 6-6.5" fill="none" stroke="#f47216" stroke-width="1.8" stroke-linecap="round" stroke-linejoin="round"/></svg>No Credit Card Required</li>
    <li><svg viewBox="0 0 20 20"><circle cx="10" cy="10" r="8.5" fill="none" stroke="#f47216" stroke-width="1.6"/><path d="M6 10.2l3 3 6-6.5" fill="none" stroke="#f47216" stroke-width="1.8" stroke-linecap="round" stroke-linejoin="round"/></svg>Pay When Bike Is Delivered</li>
    <li><svg viewBox="0 0 20 20"><circle cx="10" cy="10" r="8.5" fill="none" stroke="#f47216" stroke-width="1.6"/><path d="M6 10.2l3 3 6-6.5" fill="none" stroke="#f47216" stroke-width="1.8" stroke-linecap="round" stroke-linejoin="round"/></svg>Speak English &amp; Thai</li>
  </ul>

  <section class="payment">
    <h2>Payment Details</h2>
    <div class="field field-name">Card Name<span class="mark"></span></div>
    <div class="field field-number">Card Number</div>
    <div class="field field-exp">Exp Date</div>
    <div class="field field-cvc">CVC</div>
    <p class="other">other options</p>
    <div class="opt opt-alt">Quillora Pay</div>
    <div class="opt opt-cash">Pay via Cash on Delivery</div>
    <div class="btn-checkout">Checkout Order</div>
  </section>

  <div class="areas"><strong>We deliver to</strong> Cherng Talay • Bangtao • Chalong • Kamala • Karon • Kata • Kathu • Nai Harn • Patong • Phuket Town • Rawai • Mai Khao</div>
</body>
</html>
```